Bright Pelvic Health Business Card

Need a business card for a surgical practice called Bright Pelvic Health. We have recently selected a logo (attached). The business card will need to have two formats:
1) One with the logo/physician name/ contact info on the front and location information on the back.
2) One in "appointment reminder card" style with the logo/ contact info/ date/ time on the front and the location information on the back.

The front side should include the following information:
- Logo
- Ravi K. Desai, MD FACOG
- phone: 469-555-0182
- fax: 1-469-555-0147
- email: admin@brightpelvic.example
- website: www.brightpelvichealth.example

The back side should have the office locations listed:
4812 Quarry Bend Dr, Plano, TX 75093
3650 Wrenfield Rd, Plano, TX 75025
2245 Brambleton Ln, Irving, TX 75038
915 S Garnet Ave B314, Dallas, TX 75201
1836 Tillman Pkwy, Grand Prairie, TX 75051
6417 Dorrance Way Dr, San Antonio, TX 78240
5920 Kessler Rd, Pasadena, TX 77504

Target Market(s)

1. Other physicians who might refer patients
2. Female patients

Industry/Entity Type

Business

Font styles to use
Other font styles liked:
• Tahoma for lettering

Requirements
Must have
• As per the instructions
Should not have
• No other images needed -- please try to keep font consistent with logo design. Can use Tahoma as the font for lettering.

```html
<!DOCTYPE html>
<html lang="en">
<head>
<meta charset="utf-8">
<title>Bright Pelvic Health – Business Card</title>
<link href="https://fonts.googleapis.com/css2?family=Noto+Sans:wght@400;600&display=swap" rel="stylesheet">
<style>
  :root {
    --backdrop: #e9ecef;
    --card-blue: #8ccbe2;
    --card-blue-light: #a3d7ea;
    --ink-blue: #2a55a3;
    --band-blue: #2552a0;
    --accent-red: #d8302b;
    --ink-dark: #1d2430;
    --watermark: rgba(60, 110, 180, 0.16);
  }
  * { box-sizing: border-box; margin: 0; padding: 0; }
  html, body { width: 1200px; height: 1200px; overflow: hidden; }
  body {
    background: var(--backdrop);
    font-family: "Noto Sans", Tahoma, sans-serif;
    position: relative;
  }
  .card {
    position: absolute;
    left: 160px;
    width: 880px;
    height: 503px;
    overflow: hidden;
    background:
      repeating-linear-gradient(0deg, rgba(255,255,255,0.06) 0 1px, transparent 1px 3px),
      linear-gradient(160deg, var(--card-blue-light), var(--card-blue));
    box-shadow: 0 6px 18px rgba(0,0,0,0.18);
  }
  .card--front { top: 50px; }
  .card--back { top: 647px; }

  .watermark {
    position: absolute;
    border-radius: 50%;
    background: var(--watermark);
  }
  .card--front .watermark { width: 300px; height: 300px; right: 80px; top: 110px; }
  .card--back .watermark { width: 360px; height: 360px; left: 260px; top: 40px; }

  .brand {
    position: absolute;
    top: 92px;
    left: 0; right: 0;
    text-align: center;
    display: flex;
    justify-content: center;
    align-items: center;
    gap: 14px;
  }
  .brand__mark {
    width: 18px; height: 18px;
    border-radius: 50%;
    background: var(--ink-blue);
  }
  .brand__name {
    font-size: 44px;
    font-weight: 400;
    color: var(--ink-blue);
    letter-spacing: 0.5px;
  }
  .rule {
    position: absolute;
    height: 3px;
    background: var(--accent-red);
  }
  .rule--top { left: 250px; right: 70px; top: 180px; }
  .rule--name { left: 60px; width: 470px; top: 308px; }

  .physician {
    position: absolute;
    left: 60px;
    top: 206px;
    line-height: 1.2;
  }
  .physician__name { font-size: 26px; color: var(--accent-red); }
  .physician__cred { font-size: 19px; color: var(--ink-blue); }
  .physician__spec { font-size: 19px; color: var(--ink-blue); }

  .contact {
    position: absolute;
    left: 82px;
    top: 322px;
    list-style: none;
    font-size: 19px;
    color: var(--ink-blue);
    line-height: 26px;
  }
  .contact li { display: flex; align-items: center; gap: 10px; }
  .contact svg { width: 17px; height: 17px; flex: none; }

  .band { position: absolute; height: 50px; }
  .card--front .band--blue { left: 0; width: 440px; bottom: 0; background: var(--band-blue); }
  .card--front .band--red { left: 440px; right: 0; bottom: 38px; height: 46px; background: var(--accent-red); }
  .card--back .band--red { left: 0; width: 440px; bottom: 38px; height: 46px; background: var(--accent-red); }
  .card--back .band--blue { left: 440px; right: 0; bottom: 0; background: var(--band-blue); }

  .locations {
    position: absolute;
    left: 200px;
    top: 88px;
    list-style: none;
    font-size: 23px;
    color: var(--ink-dark);
    line-height: 35px;
  }
  .locations li { display: flex; align-items: center; gap: 16px; }
  .locations li::before {
    content: "";
    width: 16px; height: 16px;
    background: var(--accent-red);
    flex: none;
  }
</style>
</head>
<body>

<section class="card card--front" aria-label="Card front">
  <div class="watermark" aria-hidden="true"></div>

  <div class="brand">
    <span class="brand__mark" aria-hidden="true"></span>
    <span class="brand__name">Bright Pelvic Health</span>
  </div>
  <div class="rule rule--top"></div>

  <div class="physician">
    <p class="physician__name">Ravi K. Desai</p>
    <p class="physician__cred">MD FACOG</p>
    <p class="physician__spec">Female Pelvic Medicine &amp; Reconstructive Surgery</p>
  </div>
  <div class="rule rule--name"></div>

  <ul class="contact">
    <li>
      <svg viewBox="0 0 24 24" aria-hidden="true"><path fill="#d8302b" d="M6.6 10.8a15 15 0 0 0 6.6 6.6l2.2-2.2c.3-.3.7-.4 1-.2 1.1.4 2.3.6 3.6.6.6 0 1 .4 1 1V20c0 .6-.4 1-1 1A17 17 0 0 1 3 4c0-.6.4-1 1-1h3.5c.6 0 1 .4 1 1 0 1.3.2 2.5.6 3.6.1.3 0 .7-.2 1z"/></svg>
      469-555-0182
    </li>
    <li>
      <svg viewBox="0 0 24 24" aria-hidden="true"><path fill="#d8302b" d="M6 3h12v5H6zM4 9h16a2 2 0 0 1 2 2v6h-4v4H6v-4H2v-6a2 2 0 0 1 2-2zm4 7v3h8v-3z"/></svg>
      1-469-555-0147
    </li>
    <li>
      <svg viewBox="0 0 24 24" aria-hidden="true"><path fill="#d8302b" d="M3 5h18v14H3zm2 2v.4l7 4.6 7-4.6V7z"/></svg>
      admin@brightpelvic.example
    </li>
    <li>
      <svg viewBox="0 0 24 24" aria-hidden="true"><circle cx="14" cy="10" r="6" fill="none" stroke="#d8302b" stroke-width="3"/><path d="M9.5 14.5 3 21" stroke="#d8302b" stroke-width="3.5" stroke-linecap="round"/></svg>
      www.brightpelvichealth.example
    </li>
  </ul>

  <div class="band band--red"></div>
  <div class="band band--blue"></div>
</section>

<section class="card card--back" aria-label="Card back">
  <div class="watermark" aria-hidden="true"></div>

  <ul class="locations">
    <li>4812 Quarry Bend Dr, Plano, TX 75093</li>
    <li>3650 Wrenfield Rd, Plano, TX 75025</li>
    <li>2245 Brambleton Ln, Irving, TX 75038</li>
    <li>915 S Garnet Ave B314, Dallas, TX 75201</li>
    <li>1836 Tillman Pkwy, Grand Prairie, TX 75051</li>
    <li>6417 Dorrance Way Dr, San Antonio, TX 78240</li>
    <li>5920 Kessler Rd, Pasadena, TX 77504</li>
  </ul>

  <div class="band band--red"></div>
  <div class="band band--blue"></div>
</section>

</body>
</html>
```